Biotech company website design

We are looking for innovative design of our upcoming website. We are a small biotechnology company in Europe dealing with life science products and services.
Updates

Please incorporate the following top level links:
ABOUT US, PRODUCTS, SERVICES, SUPPLIERS, NEWS AND PROMOS, CONTACT US

Target Market(s)

Science people, hospitals, universities ....

Industry/Entity Type

It Company

Requirements
Must have
• Must incorporate our current logo (its color toning)

```html
<!DOCTYPE html>
<html lang="en">
<head>
<meta charset="utf-8">
<title>Linden BioWorks</title>
<link href="https://fonts.googleapis.com/css2?family=Roboto:wght@300;400;500;700&display=swap" rel="stylesheet">
<style>
:root{
  --green-dark:#1e4d0f;
  --green:#5aa524;
  --green-mid:#4f9a27;
  --lime:#a8d321;
  --lime-pale:#d6ec93;
  --charcoal:#2e3135;
  --grey-bg:#ebebeb;
  --grey-field:#8a8a8a;
  --text:#4a4a4a;
  --white:#ffffff;
}
*{margin:0;padding:0;box-sizing:border-box}
html,body{width:756px;height:1200px;overflow:hidden}
body{font-family:"Roboto",Arial,sans-serif;color:var(--text);background:var(--white);position:relative}
.abs{position:absolute}
.shapes{position:absolute;left:0;top:0}

/* header */
.header{left:0;top:0;width:756px;height:313px;background:linear-gradient(#f6f6f6,#e9e9e9)}
.hero-photo{left:370px;top:0;width:386px;height:313px;background:linear-gradient(90deg,rgba(233,233,233,1) 0%,rgba(200,170,160,.55) 30%,#c49a8c 60%,#b7b7b0 100%)}
.top-tabs{left:458px;top:0;height:22px;display:flex;font-size:10px;color:var(--white)}
.tab-shop{width:60px;height:22px;background:var(--green-dark);clip-path:polygon(8px 0,100% 0,calc(100% - 8px) 100%,0 100%);display:flex;align-items:center;justify-content:center}
.tab-login{width:100px;height:22px;margin-left:-4px;background:var(--green);clip-path:polygon(8px 0,100% 0,calc(100% - 8px) 100%,0 100%);display:flex;align-items:center;justify-content:center}
.brand{left:45px;top:40px;width:116px;display:flex;flex-direction:column;align-items:center}
.brand-mark{width:26px;height:26px;background:var(--green);margin-bottom:8px}
.brand-name{font-size:12.5px;color:var(--charcoal);background:var(--white);padding:3px 6px;white-space:nowrap}
.main-nav{left:43px;top:113px;width:111px;list-style:none;text-align:center;font-size:11.5px;color:var(--charcoal)}
.main-nav li{height:24px;line-height:20px}
.main-nav .active{background:var(--green);color:var(--white);font-weight:500}
.hero-title{left:196px;top:64px;color:var(--green-dark);line-height:1}
.hero-title .l1{display:block;font-size:44px}
.hero-title .l2{display:block;font-size:30px;margin-top:8px}
.hero-tagline{left:198px;top:155px;width:290px;font-size:14.5px;line-height:18px;color:#1a1a1a}
.btn-read{left:194px;top:222px;width:173px;height:36px;background:var(--green);color:var(--white);font-size:21px;display:flex;align-items:center;justify-content:center}
.slider-dots{left:194px;top:278px;display:flex;gap:2px}
.slider-dots span{width:11px;height:11px;background:#c7dfb4}
.slider-dots span:first-child{background:var(--green)}

/* products */
.products{left:0;top:313px;width:756px;height:119px;background:var(--charcoal)}
.products-title{left:42px;top:348px;font-size:21px;line-height:25px;color:var(--lime);font-weight:500}
.product{top:326px;width:86px;text-align:center;color:var(--white)}
.product-photo{width:86px;height:64px;border:1.5px solid var(--white);background:radial-gradient(circle at 50% 45%,#d9e8d2 0,#9cc77f 28%,#3e8f1f 70%)}
.product-name{font-size:10.5px;font-weight:700;margin-top:8px}
.product-more{font-size:7.5px;margin-top:1px}
.arrow-btn{left:566px;top:366px;width:46px;height:27px;background:var(--lime)}

/* welcome */
.welcome{left:43px;top:470px;width:375px}
.welcome h2{font-size:15.5px;font-weight:300;color:var(--charcoal);margin-bottom:8px}
.welcome p{font-size:9.2px;line-height:12.5px;color:var(--text);margin-bottom:8px}
.welcome a{font-size:9.5px;color:var(--green);text-decoration:underline}
.services{left:469px;top:458px;width:188px;height:172px;background:var(--green-dark);padding:12px 11px}
.services h3{font-size:15px;font-weight:500;color:var(--lime);margin-bottom:8px}
.services ul{list-style:none}
.services li{font-size:11px;color:var(--white);height:24px;display:flex;align-items:center;gap:7px}
.services li::before{content:"\2192";color:var(--lime);font-size:11px}

/* news */
.news-title{left:43px;top:696px;font-size:10.5px;color:var(--charcoal)}
.news-item{left:43px;width:335px;display:flex;gap:8px}
.news-photo{width:95px;height:47px;flex:none;background:linear-gradient(90deg,#1f3a10,#7fc236 55%,#cfeaa4 80%,#274a12)}
.news-body{font-size:8.2px;line-height:11px;color:var(--text);position:relative;width:232px}
.news-date{color:var(--green);font-size:9px;margin-bottom:1px}
.news-more{position:absolute;right:0;bottom:0;color:#222;font-weight:500}
.archives{left:481px;top:719px;font-size:10.5px;color:var(--charcoal)}
.archives ul{list-style:none;margin-top:8px;font-size:8px;color:var(--text)}
.archives li{height:18px}

/* suppliers */
.suppliers-title{left:42px;top:875px;font-size:21px;font-weight:300;color:var(--charcoal)}
.partner{top:872px;height:36px;background:rgba(255,255,255,.55);border-radius:3px}

/* footer */
.footer{left:0;top:921px;width:756px;height:279px;background:var(--charcoal)}
.foot-brand{left:82px;top:952px;display:flex;align-items:center;gap:8px;font-size:13px;color:var(--white)}
.foot-brand i{width:22px;height:22px;background:#b9b9b9;display:block}
.foot-address{left:80px;top:996px;font-size:9.5px;line-height:12px;color:var(--white)}
.social{left:80px;top:1058px;display:flex;gap:3px}
.social span{width:20px;height:20px;background:#5fb3d6}
.social span:nth-child(2){background:#4a7bbf}
.social span:nth-child(3){background:#6aa8c7}
.world-map{left:72px;top:1092px;width:108px;height:50px;background:radial-gradient(ellipse,#3a3e43 30%,transparent 72%)}
.contact-title{left:301px;top:956px;font-size:13.5px;font-weight:500;color:var(--white)}
.field-label{left:301px;font-size:10.5px;color:var(--white)}
.field{left:395px;width:217px;background:var(--grey-field)}
.btn-submit{left:541px;top:1131px;width:71px;height:26px;background:var(--green);color:var(--white);font-size:12.5px;display:flex;align-items:center;justify-content:center}
.bottom-bar{left:30px;top:1170px;width:695px;height:30px;background:var(--lime-pale);clip-path:polygon(12px 0,100% 0,calc(100% - 32px) 100%,0 100%)}
.copyright{left:44px;top:1180px;font-size:8.3px;color:#222}
.foot-links{left:421px;top:1181px;font-size:8.3px;color:#222}
</style>
</head>
<body>

<div class="abs header"></div>
<div class="abs hero-photo" role="img" aria-label="Photograph of the company research building with entrance stairs"></div>

<svg class="shapes" width="756" height="1200" viewBox="0 0 756 1200" aria-hidden="true">
  <!-- right-side green diagonals in hero -->
  <polygon points="756,190 756,313 620,313" fill="#5aa524" opacity=".75"/>
  <!-- middle background -->
  <rect x="0" y="432" width="756" height="260" fill="#ebebeb"/>
  <polygon points="640,313 756,313 756,432 580,432" fill="#d9d9d9"/>
  <polygon points="0,660 40,660 380,700 756,692 756,858 0,858" fill="#ffffff"/>
  <polygon points="0,690 40,660 756,720 756,858 0,858" fill="#ffffff"/>
  <polygon points="610,432 700,300 756,260 756,432" fill="#dcdcdc"/>
  <!-- big green blade -->
  <polygon points="756,205 756,690 740,695 612,470" fill="#7bb93a"/>
  <polygon points="560,458 657,458 745,648 657,648" fill="#4f9a27"/>
  <!-- left arrow tip -->
  <polygon points="0,452 22,490 0,528" fill="#a8d321"/>
  <!-- news right grey panel -->
  <polygon points="700,720 756,700 756,858 712,858" fill="#e2e2e2"/>
  <!-- suppliers band -->
  <rect x="0" y="858" width="756" height="63" fill="#a8d321"/>
  <polygon points="697,858 756,858 756,921 655,921" fill="#2e3135"/>
</svg>

<div class="abs top-tabs"><div class="tab-shop">Shop</div><div class="tab-login">Member Login</div></div>

<div class="abs brand"><span class="brand-mark"></span><span class="brand-name">Linden BioWorks</span></div>

<ul class="abs main-nav">
  <li class="active">Home</li><li>About Us</li><li>Products</li><li>Services</li><li>Suppliers</li><li>News &amp; Promos</li><li>Contact Us</li>
</ul>

<h1 class="abs hero-title"><span class="l1">Linden</span><span class="l2">BioWorks</span></h1>
<p class="abs hero-tagline">is an innovative company focused on developing tools for acceleration of research and applications in the field of Life Sciences.</p>
<div class="abs btn-read">READ MORE</div>
<div class="abs slider-dots"><span></span><span></span><span></span></div>

<div class="abs products"></div>
<h2 class="abs products-title">OUR<br>PRODUCTS</h2>
<div class="abs product" style="left:201px"><div class="product-photo" role="img" aria-label="Product bottles on green background"></div><div class="product-name">GENEFORM®</div><div class="product-more">READ MORE</div></div>
<div class="abs product" style="left:319px"><div class="product-photo" role="img" aria-label="Product bottles on green background"></div><div class="product-name">GENEFORM®</div><div class="product-more">READ MORE</div></div>
<div class="abs product" style="left:440px"><div class="product-photo" role="img" aria-label="Product bottles on green background"></div><div class="product-name">GENEFORM®</div><div class="product-more">READ MORE</div></div>
<div class="abs arrow-btn"><svg width="46" height="27" viewBox="0 0 46 27" aria-hidden="true"><path d="M16 13.5h13M24 8.5l5 5-5 5" stroke="#fff" stroke-width="2" fill="none"/></svg></div>

<section class="abs welcome">
  <h2>Welcome to Our Website</h2>
  <p>Lorem Ipsum is simply dummy text of the printing and typesetting industry. Lorem Ipsum has been the industry's standard dummy text ever since the 1500s, when an unknown printer took a galley of type and scrambled it to make a type specimen book.</p>
  <p>It has survived not only five centuries, but also the leap into electronic typesetting, remaining essentially unchanged. It was popularised in the 1960s with the release of Letraset sheets containing Lorem Ipsum passages.</p>
  <a>Read More About Linden BioWorks</a>
</section>

<section class="abs services">
  <h3>OUR SERVICES</h3>
  <ul><li>DNA Sequencing</li><li>DNA Forensic Analysis</li><li>Services Link 1</li><li>Services Link 2</li><li>Other Services</li></ul>
</section>

<h3 class="abs news-title">Latest News:</h3>
<article class="abs news-item" style="top:716px">
  <div class="news-photo" role="img" aria-label="Close-up of glowing laboratory tube"></div>
  <div class="news-body"><div class="news-date">09-29-2013</div>Lorem Ipsum is simply dummy text of the printing and typesetting industry. Lorem Ipsum has been the industry's standard dummy text ever since the 1500s.<span class="news-more">+ Read More</span></div>
</article>
<article class="abs news-item" style="top:778px">
  <div class="news-photo" role="img" aria-label="Close-up of glowing laboratory tube"></div>
  <div class="news-body"><div class="news-date">09-28-2013</div>Lorem Ipsum is simply dummy text of the printing and typesetting industry. Lorem Ipsum has been the industry's standard dummy text ever since the 1500s.<span class="news-more">+ Read More</span></div>
</article>
<div class="abs archives">Archives:
  <ul><li>- August 2013</li><li>- July 2013</li><li>- June 2013</li><li>- May 2013</li><li>- April 2013</li></ul>
</div>

<h2 class="abs suppliers-title">Our Suppliers</h2>
<div class="abs partner" style="left:192px;width:106px"></div>
<div class="abs partner" style="left:318px;width:58px"></div>
<div class="abs partner" style="left:392px;width:30px"></div>
<div class="abs partner" style="left:438px;width:82px"></div>
<div class="abs partner" style="left:533px;width:78px"></div>

<div class="abs footer"></div>
<div class="abs foot-brand"><i></i>Linden BioWorks</div>
<address class="abs foot-address" style="font-style:normal">Linden BioWorks, s.r.o.<br>ul. Lipová 12, 110 00 Prague<br>Czech Republic<br>Email: info@lindenbioworks.com</address>
<div class="abs social"><span></span><span></span><span></span></div>
<div class="abs world-map" role="img" aria-label="Faint world map"></div>

<h3 class="abs contact-title">Quick Contact:</h3>
<span class="abs field-label" style="top:993px">Your Name:</span>
<div class="abs field" style="top:985px;height:28px"></div>
<span class="abs field-label" style="top:1033px">Your Email:</span>
<div class="abs field" style="top:1024px;height:28px"></div>
<span class="abs field-label" style="top:1084px">Message:</span>
<div class="abs field" style="top:1063px;height:57px"></div>
<div class="abs btn-submit">SUBMIT</div>

<div class="abs bottom-bar"></div>
<p class="abs copyright">Copyright 2007-2013 Linden BioWorks | All Rights Reserved</p>
<p class="abs foot-links">Home - About Us - Products - Services - Contact Us</p>

</body>
</html>
```